Lumo Care — Premium Telehealth Marketing Website

Lumo Care is a modern, cash-pay telehealth brand offering prescription weight-loss (GLP-1) and sexual-health treatment online, with licensed US providers — no insurance required. We're building a premium, trustworthy direct-to-consumer healthcare brand in the same tier as Welk, Tu, and Orla.

We need a clean, modern, premium marketing website design — warm and trustworthy, not cold or clinical. Think high-end wellness brand: generous whitespace, elegant typography, calm and confident. It should feel medically credible but human and approachable.

WHAT WE NEED DESIGNED (3 core templates that define the whole site):

1. Homepage — the brand showcase that establishes the full visual language (hero, sections, product highlights, how-it-works, trust elements, footer).

2. Product / Treatment page template — a reusable layout for any medication (transparent pricing, how it works, what's included, clinical info, safety, clear call-to-action). We'll reuse this pattern for all treatments.

3. Interior / Content page template — a flexible layout for sub-pages like How It Works, About, Contact, FAQ, and legal pages.

We'll implement the final site ourselves in React/Next.js + Tailwind CSS, so clean, well-structured design (and HTML/CSS if you provide it) is a strong plus.

BRAND DIRECTION (already established — please design within this):

- Logo: lowercase wordmark "lumo." with the period in gold (see attached). Please build the design around this existing logo.
- Colors: deep navy (#0B1B33 and #14315C) with a warm gold accent (#E0A458); soft light backgrounds (#EEF3F9, #FBFCFE).
- Typography: a refined serif for headlines (e.g., Fraunces) paired with a clean sans-serif for body (e.g., Inter).
- Tone: premium, warm, trustworthy, human.

INSPIRATION / QUALITY BAR: Welk (welk.example), Tu (tu.example), Orla — the polished DTC healthcare aesthetic. We want that tier of quality, with our own warmer navy-and-gold identity.

Industry/Entity Type

Telemedicine

Coding

Coded - Design and coding required

Number of Pages Required

3 page

Requirements
Nice to have
• Side Scrolling Medictions bar like on Tu.example

```html
<!DOCTYPE html>
<html lang="en">
<head>
<meta charset="utf-8">
<title>Lumo Care — Telehealth</title>
<link href="https://fonts.googleapis.com/css2?family=Fraunces:opsz,wght@9..144,500;9..144,600&family=Inter:wght@400;500;600&display=swap" rel="stylesheet">
<style>
  :root{
    --navy:#0B1B33;
    --navy-2:#14315C;
    --gold:#E0A458;
    --soft:#EEF3F9;
    --page:#FBFCFE;
    --white:#FFFFFF;
    --text:#4A5566;
    --muted:#8A909A;
    --line:#E7EBF1;
  }
  *{box-sizing:border-box;margin:0;padding:0}
  html,body{width:752px;height:1200px;overflow:hidden}
  body{background:var(--page);font-family:"Inter",sans-serif;color:var(--navy);position:relative}
  .serif{font-family:"Fraunces",serif}
  .abs{position:absolute}

  /* header */
  .site-header{position:absolute;left:0;top:0;width:752px;height:42px;background:var(--white);border-bottom:1px solid var(--line)}
  .brand{position:absolute;left:18px;top:13px;font-family:"Inter",sans-serif;font-weight:600;font-size:12px;color:var(--navy)}
  .main-nav a{position:absolute;top:15px;font-size:9px;color:var(--navy-2);text-decoration:none;font-weight:500}
  .main-nav a.active{color:var(--navy)}
  .main-nav a.active::after{content:"";position:absolute;left:0;right:0;top:15px;height:1.5px;background:var(--gold)}
  .btn-login{position:absolute;left:623px;top:12px;width:41px;height:18px;border:1px solid var(--navy);border-radius:9px;font-size:7.5px;display:flex;align-items:center;justify-content:center}
  .btn-start{position:absolute;left:673px;top:13px;width:61px;height:16px;background:var(--gold);color:var(--white);border-radius:8px;font-size:7.5px;display:flex;align-items:center;justify-content:center}

  /* hero */
  .eyebrow{left:55px;top:89px;font-size:7.3px;letter-spacing:1px;color:var(--gold);font-weight:600}
  .hero-title{left:55px;top:108px;font-size:26px;line-height:33px;font-weight:600;width:290px}
  .hero-title .accent{color:var(--gold)}
  .hero-copy{left:55px;top:187px;width:275px;font-size:9.6px;line-height:16px;color:var(--text)}
  .btn-primary{left:55px;top:253px;width:102px;height:22px;border-radius:11px;background:var(--gold);color:var(--white);font-size:7.3px;font-weight:500;display:flex;align-items:center;justify-content:center}
  .hero-media{left:390px;top:70px;width:308px;height:223px;border-radius:10px;background:linear-gradient(135deg,#e9eaec 0%,#cfd2d6 45%,#5a4a42 70%,#d8dadd 100%)}

  /* trust strip */
  .trust{left:55px;top:337px;width:642px;height:112px;background:var(--white);border-radius:14px;box-shadow:0 2px 10px rgba(11,27,51,.04)}
  .trust-label{position:absolute;left:0;right:0;top:28px;text-align:center;font-size:6.2px;letter-spacing:1px;color:var(--muted);font-weight:600}
  .trust-name{position:absolute;top:58px;transform:translateX(-50%);font-size:15px;color:var(--muted);font-weight:500}

  /* treatments */
  .treatments{left:55px;top:493px;width:642px;height:300px;background:var(--soft);border-radius:14px;overflow:hidden}
  .section-title{position:absolute;left:0;right:0;text-align:center;font-size:20px;font-weight:600;color:var(--navy)}
  .treat-card{position:absolute;top:78px;width:144px;height:177px;background:var(--white);border-radius:7px}
  .treat-card.clipped{width:139px;border-radius:7px 0 0 7px}
  .treat-icon{position:absolute;left:13px;top:13px;width:27px;height:27px;border-radius:50%;background:var(--soft);display:flex;align-items:center;justify-content:center}
  .treat-name{position:absolute;left:13px;top:51px;font-size:10px;font-weight:600}
  .treat-sub{position:absolute;left:13px;top:68px;font-size:7.8px;color:var(--text)}
  .treat-bar{position:absolute;left:13px;top:85px;width:27px;height:2px;background:var(--gold);border-radius:1px}
  .treat-rule{position:absolute;left:13px;right:13px;top:140px;height:1px;background:var(--line)}
  .treat-link{position:absolute;left:13px;top:151px;font-size:9px;color:var(--navy-2);font-weight:500}
  .scrollbar{position:absolute;left:14px;top:265px;width:615px;height:9px;background:#F1F1F1}
  .scroll-thumb{position:absolute;left:9px;top:0;width:448px;height:9px;background:#C4C4C4}
  .scroll-arrow{position:absolute;top:0;font-size:9px;color:#555;line-height:9px}

  /* steps */
  .steps-title{top:843px}
  .steps-bar{left:354px;top:875px;width:45px;height:2px;background:var(--gold)}
  .step-card{position:absolute;top:905px;width:201px;height:123px;background:var(--white);border:1px solid #F0F2F6;border-radius:7px;text-align:center}
  .step-num{position:absolute;left:85px;top:17px;width:31px;height:31px;border-radius:50%;background:var(--navy);color:var(--white);font-family:"Fraunces",serif;font-size:11px;display:flex;align-items:center;justify-content:center}
  .step-title{position:absolute;left:0;right:0;top:59px;font-size:11px;font-weight:500}
  .step-copy{position:absolute;left:14px;right:14px;top:79px;font-size:8.3px;line-height:13.5px;color:var(--text)}

  /* footer */
  .site-footer{left:0;top:1073px;width:752px;height:127px;background:var(--navy);color:var(--white)}
  .footer-brand{position:absolute;left:55px;top:30px;font-family:"Inter",sans-serif;font-weight:600;font-size:12px;color:var(--white)}
  .footer-tag{position:absolute;left:55px;top:53px;font-size:8px}
  .footer-col{position:absolute;top:27px}
  .footer-col h4{font-size:9px;font-weight:600;margin-bottom:9px}
  .footer-col p{font-size:8px;line-height:17px}
</style>
</head>
<body>

<header class="site-header">
  <div class="brand">lumo.</div>
  <nav class="main-nav">
    <a class="active" style="left:277px">Home</a>
    <a style="left:316px">Treatment</a>
    <a style="left:372px">About</a>
  </nav>
  <div class="btn-login">Login</div>
  <div class="btn-start">Get Started</div>
</header>

<div class="abs eyebrow">TELEHEALTH, SIMPLIFIED</div>
<h1 class="abs hero-title serif">Weight Loss &amp; Sexual Health, <span class="accent">Clarified</span>.</h1>
<p class="abs hero-copy">Lumo connects you with licensed US providers for prescription weight loss and sexual health treatments. No insurance, no hassle, just care.</p>
<div class="abs btn-primary">Find Your Treatment</div>
<div class="abs hero-media" role="img" aria-label="Photo of a doctor in a white coat with a stethoscope holding a smartphone"></div>

<section class="abs trust">
  <div class="trust-label">TRUSTED BY PATIENTS ACROSS THE US</div>
  <span class="trust-name" style="left:189px">Welk</span>
  <span class="trust-name" style="left:268px">TU</span>
  <span class="trust-name" style="left:347px">Orla</span>
  <span class="trust-name" style="left:444px">Caravel</span>
</section>

<section class="abs treatments">
  <h2 class="section-title serif" style="top:31px">Our Treatments</h2>

  <article class="treat-card" style="left:14px">
    <div class="treat-icon"><svg width="14" height="16" viewBox="0 0 14 16"><path d="M7 1v13M2 9l5 5 5-5" fill="none" stroke="#0B1B33" stroke-width="1.4"/></svg></div>
    <div class="treat-name">GLP-1 Weight Loss</div>
    <div class="treat-sub">Starting at $149/mo</div>
    <div class="treat-bar"></div><div class="treat-rule"></div>
    <div class="treat-link">View Treatment →</div>
  </article>

  <article class="treat-card" style="left:172px">
    <div class="treat-icon"><svg width="12" height="18" viewBox="0 0 12 18"><rect x="2" y="1" width="8" height="5" fill="none" stroke="#0B1B33" stroke-width="1.4"/><rect x="2" y="11" width="8" height="5" fill="none" stroke="#0B1B33" stroke-width="1.4"/></svg></div>
    <div class="treat-name">Semaglutide</div>
    <div class="treat-sub">Weight management</div>
    <div class="treat-bar"></div><div class="treat-rule"></div>
    <div class="treat-link">View Treatment →</div>
  </article>

  <article class="treat-card" style="left:330px">
    <div class="treat-icon"><svg width="18" height="12" viewBox="0 0 18 12"><path d="M1 4h16M9 1v4M9 5l-5 6M9 5l5 6" fill="none" stroke="#0B1B33" stroke-width="1.3"/></svg></div>
    <div class="treat-name">Tirzepatide</div>
    <div class="treat-sub">Weight management</div>
    <div class="treat-bar"></div><div class="treat-rule"></div>
    <div class="treat-link">View Treatment →</div>
  </article>

  <article class="treat-card clipped" style="left:489px">
    <div class="treat-icon"><svg width="22" height="20" viewBox="0 0 22 20"><path d="M11 18C4 13 1 10 1 6a5 5 0 0 1 10-1 5 5 0 0 1 10 1c0 4-3 7-10 12z" fill="none" stroke="#0B1B33" stroke-width="1.5"/></svg></div>
    <div class="treat-name">Sexual Health</div>
    <div class="treat-sub">Telehealth for men &amp; women</div>
    <div class="treat-bar"></div><div class="treat-rule"></div>
    <div class="treat-link">View Treatment →</div>
  </article>

  <div class="scrollbar">
    <span class="scroll-arrow" style="left:1px">‹</span>
    <div class="scroll-thumb"></div>
    <span class="scroll-arrow" style="right:1px">›</span>
  </div>
</section>

<h2 class="section-title serif steps-title">It's simple to get started</h2>
<div class="abs steps-bar"></div>

<article class="step-card" style="left:55px">
  <div class="step-num">1</div>
  <div class="step-title">Sign Up</div>
  <div class="step-copy">Complete a brief health questionnaire.</div>
</article>
<article class="step-card" style="left:275px">
  <div class="step-num">2</div>
  <div class="step-title">Get Prescribed</div>
  <div class="step-copy">Receive a personalized prescription from a licensed US provider.</div>
</article>
<article class="step-card" style="left:496px">
  <div class="step-num">3</div>
  <div class="step-title">Receive &amp; Thrive</div>
  <div class="step-copy">Medication delivered to your door with ongoing support.</div>
</article>

<footer class="abs site-footer">
  <div class="footer-brand">lumo.</div>
  <div class="footer-tag">Premium telehealth for the modern age.</div>
  <div class="footer-col" style="left:308px"><h4>Company</h4><p>About</p><p>Careers</p><p>Press</p></div>
  <div class="footer-col" style="left:444px"><h4>Products</h4><p>Weight Loss</p><p>Sexual Health</p><p>Wellness</p></div>
  <div class="footer-col" style="left:579px"><h4>Support</h4><p>Help Center</p><p>Contact</p><p>Privacy Policy</p></div>
</footer>

</body>
</html>
```